Flyer for an online formula one racing league

Hello.

I am looking for the perfect one page facebook/instagram style flyer for an online formula one racing league. The racing league is called 'VOLTA RACING LEAGUE'.

Information that MUST be on the new flyer is already on the old flyer I have uploaded here. In addition to including: The Volta racing league 'V' logo I have uploaded AND the text: 'Very popular, clean and competitive racing league, running for its 4th season. Why not join with a friend? Race times, Mondays, Tuesdays and Wednesdays each at 8pm UK TIME Message below for any questions. (Spacing of information is not important, however all the information in regards to the racing I have just mentioned MUST BE on the flyer, this includes info from old pic, logo and the other info I just mentioned).

It would be beneficial to have lots of dark blue on the flyer and the new flyer to be a lot different to the original flyer I uploaded, but this is not essential.

I apologise if I did not explain very well, any questions, please message me.

The best flyer should look the most attractive to someone that might be interested in joining an online formula one racing league.

I used this website before to create the perfect logo for my Sunday League team last year, and I was very impressed. I look forward to seeing your submissions.

Target Market(s)

No specific target, more something that may attract someone into joining a formula one online racing league

Industry/Entity Type

e sports/formula one

Colors
0054AA
0677BA
7BADD7
CADEEF
E8F1F8

Requirements
Must have
• Read product description please
Should not have
• Ignoring product description!

```html
<!DOCTYPE html>
<html lang="en">
<head>
<meta charset="UTF-8">
<title>Volta Racing League – Season 4</title>
<link href="https://fonts.googleapis.com/css2?family=Anton&family=Archivo:ital,wght@0,600;1,500&family=Great+Vibes&display=swap" rel="stylesheet">
<style>
  :root {
    --backdrop: #a9c1cc;
    --navy: #0a1130;
    --navy-deep: #060b22;
    --pink: #ff1a9c;
    --white: #ffffff;
    --fire: #f08a3a;
    --ember: #d2503a;
    --smoke: #6a86b4;
  }
  * { margin: 0; padding: 0; box-sizing: border-box; }
  html, body {
    width: 1200px; height: 699px; overflow: hidden;
    background: var(--backdrop);
  }
  .flyer {
    position: absolute; left: 78px; top: 77px;
    width: 1044px; height: 546px;
    background: var(--navy);
    overflow: hidden;
    box-shadow: 0 18px 40px rgba(20, 40, 60, 0.35);
  }
  .race-photo {
    position: absolute; left: 380px; top: 0; width: 664px; height: 546px;
    background:
      radial-gradient(ellipse 30% 35% at 90% 42%, rgba(255,170,80,0.9), transparent 70%),
      radial-gradient(ellipse 35% 28% at 55% 68%, rgba(210,80,50,0.7), transparent 70%),
      radial-gradient(ellipse 40% 35% at 38% 50%, rgba(160,185,225,0.55), transparent 70%),
      linear-gradient(180deg, var(--navy) 0%, #2a3458 35%, #3a2f48 70%, var(--fire) 100%);
    -webkit-mask-image: linear-gradient(90deg, transparent 0%, #000 32%);
    mask-image: linear-gradient(90deg, transparent 0%, #000 32%);
  }
  .flag-stripe {
    position: absolute; left: 0; top: 38px; width: 152px; height: 66px;
    background: linear-gradient(90deg, rgba(255,255,255,0.05), rgba(255,255,255,0.8));
  }
  .league-title {
    position: absolute; left: 158px; top: 32px;
    font-family: "Anton", sans-serif; font-size: 72px; line-height: 1;
    color: var(--white); letter-spacing: 0.5px; white-space: nowrap;
    transform: skewX(-8deg); transform-origin: left bottom;
  }
  .brand-mark {
    position: absolute; left: 858px; top: 62px;
    display: flex; align-items: center; gap: 12px;
  }
  .brand-mark .mark-square { width: 24px; height: 24px; background: var(--pink); }
  .brand-mark .mark-name {
    font-family: "Anton", sans-serif; font-size: 54px; line-height: 1; color: var(--white);
  }
  .tagline {
    position: absolute; left: 13px; top: 126px; width: 400px;
    font-family: "Archivo", sans-serif; font-style: italic; font-weight: 500;
    font-size: 25px; line-height: 28px; color: var(--pink); text-align: right;
  }
  .season {
    position: absolute; left: 39px; top: 193px;
    font-family: "Anton", sans-serif; font-size: 86px; line-height: 1;
    color: var(--pink); transform: skewX(-6deg); transform-origin: left bottom;
    white-space: nowrap;
  }
  .invite {
    position: absolute; left: 52px; top: 288px;
    font-family: "Great Vibes", cursive; font-size: 62px; line-height: 56px;
    color: var(--white); white-space: nowrap;
  }
  .invite span { display: block; padding-left: 66px; }
  .schedule {
    position: absolute; left: 39px; top: 419px; width: 331px; height: 77px;
    display: flex; border: 2px solid var(--white);
    font-family: "Archivo", sans-serif; font-weight: 600; text-align: center;
  }
  .schedule .days {
    width: 173px; background: var(--navy-deep); color: var(--white);
    display: flex; align-items: center; justify-content: center;
    font-size: 28px; line-height: 30px;
  }
  .schedule .time {
    flex: 1; background: var(--white); color: var(--navy);
    display: flex; flex-direction: column; align-items: center; justify-content: center;
  }
  .schedule .time strong { font-size: 29px; line-height: 30px; font-weight: 600; }
  .schedule .time small { font-size: 23px; line-height: 25px; font-weight: 500; }
</style>
</head>
<body>
  <main class="flyer">
    <div class="race-photo" role="img" aria-label="Photo of a formula car racing towards the viewer through smoke and sparks"></div>
    <div class="flag-stripe" role="img" aria-label="Chequered flag motion streak"></div>
    <h1 class="league-title">VOLTA RACING LEAGUE</h1>
    <div class="brand-mark"><span class="mark-square"></span><span class="mark-name">VOLTA</span></div>
    <p class="tagline">Popular, Clean &amp; Competitive Racing League, Running for its</p>
    <h2 class="season">4TH SEASON</h2>
    <p class="invite">Why not join <span>with a friend?</span></p>
    <div class="schedule">
      <div class="days">Mon, Tue<br>&amp; Wed</div>
      <div class="time"><strong>8PM</strong><small>UK TIME</small></div>
    </div>
  </main>
</body>
</html>
```